CalmPath Nurses' Manifesto

Design a manifesto to inspire and motivate nurses to work at minimum standards of excellence in their nursing practice.

The manifesto will become a feature of our website, at conferences, workshops and retreats. It will also be featured on other marketing tools.

Primary Market:
Nurses and/or other healthcare professionals (specifically Doctors, Occupational Therapists, Psychologists and Social Workers).

However the manifesto is equally applicable to all nurses and healthcare professionals from new graduates to very experienced senior clinicians, administration officers,managers and healthcare executive personnel.

Mainly females and primarily 35 to 65 years old, which suggests people in this target age group have extensive experience, but have become jaded'.

The purpose of our business is to assist healthcare professionals, primarily nurses, to maintain their enthusiasm and excellence in service provision, for their benefit as well as the benefit of the clients.

I have attached:
File 1: Copy Samples and examples: which has the copy for the manifesto, examples that appeal to us and our 3 attempts.
File 2: Our colour Spec Sheet, HOWEVER the colours are not necessary limited to these colours. These colours are not in the logo that will be on the manifesto. The colours on the logo attached can/or also be used.
File 3: Prototype logo. The final logo will be available within 3 to 4 days.

Requirements
Must have
• Must use the copy as per the attached file.

It should be contemporary, eye catching and motivational.

Sample 1 on the attached file (File 3: copy, samples and examples_554207 saturday, 29 june 2013 06:24:3030) Is close to what we are looking for.
Should not have
• MUST BE EASY TO READ. Each line MUST be clearly defined from each other.

```html
<!DOCTYPE html>
<html lang="en">
<head>
<meta charset="utf-8">
<title>CalmPath Nurses' Manifesto</title>
<link rel="stylesheet" href="https://fonts.googleapis.com/css2?family=Alfa+Slab+One&family=Roboto+Slab:wght@700;900&family=Varela+Round&family=Nunito:wght@600&family=Gelasio:wght@400;600&family=Cookie&family=Audiowide&family=Oswald:wght@700&family=Open+Sans:wght@400;600;700&family=Raleway:wght@400&family=Courier+Prime:wght@700&family=Inconsolata:wght@400&family=Share+Tech+Mono&family=Kurale&family=Comfortaa:wght@400&display=swap">
<style>
  :root {
    --board: #3b5756;
    --white: #ffffff;
    --orange: #f49a4a;
    --lime: #9ccb4b;
    --green: #3aa35a;
    --grey: #a3a8a8;
    --teal: #3fb8ad;
    --teal-soft: #5fc2b4;
  }
  * { margin: 0; padding: 0; box-sizing: border-box; }
  html, body { width: 900px; height: 1200px; overflow: hidden; background: var(--board); }
  .manifesto { position: relative; width: 900px; height: 1200px; background: var(--board); overflow: hidden; }
  .line { position: absolute; white-space: nowrap; line-height: 1; }

  .title { left: 106px; top: 26px; font-family: "Alfa Slab One", serif; font-weight: 400; font-size: 56px; color: var(--white); letter-spacing: 2px; }
  .open-hands { left: 110px; top: 94px; font-family: "Varela Round", sans-serif; font-size: 36px; color: var(--orange); }
  .delight { font-family: "Nunito", sans-serif; font-weight: 600; font-size: 34px; color: var(--lime); }
  .delight-1 { left: 110px; top: 146px; }
  .delight-2 { left: 385px; top: 187px; }
  .delight-3 { left: 488px; top: 227px; }
  .learn-big { left: 100px; top: 190px; font-family: "Roboto Slab", serif; font-weight: 700; font-size: 80px; color: var(--grey); }
  .learn-rest { left: 104px; top: 272px; font-family: "Roboto Slab", serif; font-weight: 700; font-size: 40px; color: var(--grey); }
  .support { left: 102px; font-family: "Gelasio", serif; font-weight: 600; font-size: 41px; color: var(--white); }
  .support-1 { top: 322px; }
  .support-2 { top: 376px; }
  .trust { left: 106px; font-family: "Cookie", cursive; font-size: 48px; letter-spacing: 3px; color: var(--lime); }
  .trust-1 { top: 424px; }
  .trust-2 { top: 470px; }
  .lifelong { left: 100px; top: 518px; font-family: "Roboto Slab", serif; font-weight: 900; font-size: 50px; color: var(--orange); }
  .diversity { left: 102px; font-family: "Audiowide", sans-serif; font-size: 25px; color: var(--green); letter-spacing: 2px; }
  .diversity-1 { top: 588px; }
  .diversity-2 { top: 617px; }
  .unique-lead { left: 102px; top: 660px; font-family: "Oswald", sans-serif; font-weight: 700; font-size: 24px; color: var(--teal); }
  .unique-lead b { font-size: 38px; vertical-align: -4px; }
  .right-thing { left: 353px; top: 652px; font-family: "Open Sans", sans-serif; font-size: 23px; color: var(--white); }
  .exception { left: 482px; top: 676px; font-family: "Open Sans", sans-serif; font-size: 58px; color: var(--white); }
  .revel { left: 102px; top: 708px; font-family: "Oswald", sans-serif; font-weight: 700; font-size: 21px; color: var(--teal); }
  .within { left: 102px; top: 740px; font-family: "Raleway", sans-serif; font-size: 45px; color: var(--lime); }
  .exceptional { left: 102px; top: 790px; font-family: "Courier Prime", monospace; font-weight: 700; font-size: 17.5px; color: var(--teal); }
  .purpose { left: 104px; font-family: "Open Sans", sans-serif; font-size: 25px; color: var(--orange); }
  .purpose-1 { top: 811px; }
  .purpose-2 { top: 845px; }
  .no-one { left: 478px; font-family: "Inconsolata", monospace; font-size: 24px; color: var(--green); }
  .no-one-1 { top: 789px; }
  .no-one-2 { top: 814px; }
  .no-one-3 { top: 839px; font-size: 36px; }
  .respond { left: 104px; font-family: "Alfa Slab One", serif; font-weight: 400; font-size: 22px; letter-spacing: 1px; color: var(--white); }
  .respond-1 { top: 884px; }
  .respond-2 { top: 920px; }
  .respond-3 { top: 956px; }
  .can-do { left: 108px; top: 987px; font-family: "Open Sans", sans-serif; font-weight: 700; font-size: 18.5px; color: var(--lime); }
  .thoughts { left: 106px; font-family: "Share Tech Mono", monospace; font-size: 32px; color: var(--green); }
  .thoughts-1 { top: 1018px; }
  .thoughts-2 { top: 1058px; }
  .dream { left: 104px; top: 1082px; font-family: "Kurale", serif; font-size: 74px; color: var(--orange); }

  .brand { position: absolute; left: 704px; top: 1112px; font-family: "Open Sans", sans-serif; font-weight: 600; font-size: 24px; line-height: 1; color: var(--white); }

  .up { position: absolute; writing-mode: vertical-rl; transform: rotate(180deg); white-space: nowrap; line-height: 1; text-align: start; }
  .down { position: absolute; writing-mode: vertical-rl; white-space: nowrap; line-height: 1; text-align: start; }

  .skillfully { left: 28px; top: 30px; height: 472px; font-family: "Oswald", sans-serif; font-weight: 700; font-size: 54px; color: var(--green); }
  .smile { font-family: "Gelasio", serif; font-size: 24px; letter-spacing: 1.5px; color: var(--white); top: 518px; height: 388px; }
  .smile-1 { left: 62px; }
  .smile-2 { left: 33px; }
  .always-be { left: 12px; top: 925px; height: 242px; font-family: "Comfortaa", sans-serif; font-size: 44px; color: var(--grey); }
  .solution { left: 58px; top: 935px; height: 232px; font-family: "Comfortaa", sans-serif; font-size: 21px; color: var(--grey); }

  .generously { left: 698px; top: 150px; height: 360px; font-family: "Cookie", cursive; font-size: 44px; color: var(--teal-soft); }
  .limits { left: 762px; top: 150px; height: 950px; font-family: "Cookie", cursive; font-size: 46px; color: var(--teal-soft); }
  .health { left: 846px; top: 14px; height: 1155px; font-family: "Gelasio", serif; font-size: 24px; letter-spacing: 0.5px; color: var(--white); }
</style>
</head>
<body>
<main class="manifesto">
  <h1 class="line title">NURSES’ MANIFESTO</h1>
  <p class="line open-hands">Nurse with open hands, hearts and minds.</p>
  <p class="line delight delight-1">Delight your clients and colleagues</p>
  <p class="line delight delight-2">by exceeding their</p>
  <p class="line delight delight-3">expectations.</p>
  <p class="line learn-big">Learn</p>
  <p class="line learn-rest">something new each day.</p>
  <p class="line support support-1">Support your colleagues</p>
  <p class="line support support-2">&amp; champion their purpose.</p>
  <p class="line trust trust-1">Trust your knowledge and seek</p>
  <p class="line trust trust-2">advice only from respected sources.</p>
  <p class="line lifelong">Be a life long learner.</p>
  <p class="line diversity diversity-1">CELEBRATE,RESPECT AND VALUE THE</p>
  <p class="line diversity diversity-2">DIVERSITY OF AUSTRALIAN CULTURE.</p>
  <p class="line unique-lead">YOU ARE <b>UNIQUE</b>,</p>
  <p class="line right-thing">Always do the right thing without</p>
  <p class="line exception">exception</p>
  <p class="line revel">REVEL IN YOUR INDIVIDUALITY.</p>
  <p class="line within">Seek success firstly from within.</p>
  <p class="line exceptional">Only follow exceptional leaders.</p>
  <p class="line purpose purpose-1">Always lead with purpose,</p>
  <p class="line purpose purpose-2">passion and commitment.</p>
  <p class="line no-one no-one-1">If there is no one</p>
  <p class="line no-one no-one-2">left to follow, then</p>
  <p class="line no-one no-one-3">lead!</p>
  <p class="line respond respond-1">Respond to complex situations innovatively,</p>
  <p class="line respond respond-2">creatively and safely within the scope of your</p>
  <p class="line respond respond-3">practice.</p>
  <p class="line can-do">Adopt a‘can do’ attitude to everything that comes your way.</p>
  <p class="line thoughts thoughts-1">CHOOSE YOUR THOUGHTS WISELY, THEY</p>
  <p class="line thoughts thoughts-2">CREATE YOUR REALITY.</p>
  <p class="line dream">Live your dream.</p>

  <p class="up skillfully">Delivercare skillfully.</p>
  <p class="up smile smile-1">Smile and infect others with</p>
  <p class="up smile smile-2">your happiness and have fun!</p>
  <p class="up always-be">Always be</p>
  <p class="up solution">solution focused.</p>

  <p class="down generously">knowledge generously.</p>
  <p class="down limits">Respect the limits of people’s knowledge and share your</p>
  <p class="down health">Look after yourself &nbsp;and value your health as much as you value the health of &nbsp;others.</p>

  <p class="brand">CalmPath</p>
</main>
</body>
</html>
```